Holiday Rental Leaflet

Want a DL size double sided leaflet to distribute via local businesses, markets, family and friends
HOLIDAY RENTALCarrickalinga - 17 Brindle Street Sleeps 8-10 (2 Queen, 1 Double, 2 bunks), 4 bedrooms, BIR to all bedrooms 2 Bathrooms, one with bath, 2 toilets Open Plan Lounge/Dining/Kitchen area Dining Table for 8 peopleReverse cycle airconditionerSlow combustion wood heaterTV/DVD, CD/RadioKitchen has m/wave, oven, fridge/freezer, dishwasherBBQ providedTimber decking with 2 outside tables and 12 chairs Washing Machine and dryer provided One street back from beach Smoke free zone No Pets
For further information or to book contact Joan on 0491 287 306 or email joanfarrow27@velmarnet.com.au

Industry/Entity Type

Kitchen

Requirements
Nice to have
• Have sent a variety of photos of the house. No need to use all of them, pick out the most relevant for the leaflet.

```html
<!DOCTYPE html>
<html lang="en">
<head>
<meta charset="utf-8">
<title>Holiday Special – Rental Leaflet</title>
<link rel="stylesheet" href="https://fonts.googleapis.com/css2?family=Montserrat:wght@400;600;800&family=Questrial&display=swap">
<style>
  :root {
    --page-bg: #f4f1e6;
    --navy: #0f3f74;
    --blue: #1c5c98;
    --blue-light: #2f86c8;
    --tab-top: #3da2dc;
    --tab-bottom: #1a67a8;
    --cyan: #1ba3d6;
    --panel: #efefef;
    --ink: #3a3a3a;
    --white: #ffffff;
  }
  * { box-sizing: border-box; margin: 0; padding: 0; }
  html, body { width: 977px; height: 1200px; overflow: hidden; }
  body { background: var(--page-bg); position: relative; font-family: "Montserrat", Arial, sans-serif; }

  .leaflet {
    position: absolute; left: 20px; top: 264px;
    width: 937px; height: 672px;
    background: var(--white);
    box-shadow: 0 4px 18px rgba(0,0,0,.18);
    overflow: hidden;
  }
  .header-band {
    position: absolute; left: 0; top: 0; width: 100%; height: 403px;
    background: linear-gradient(180deg, var(--blue) 0%, var(--navy) 100%);
  }
  .header-band::after {
    content: ""; position: absolute; left: 0; right: 0; top: 143px; height: 2px;
    background: rgba(255,255,255,.08);
  }
  .title-tab {
    position: absolute; left: 108px; top: 32px; width: 738px; height: 111px;
    border-radius: 22px 22px 0 0;
    background: linear-gradient(180deg, var(--tab-top) 0%, var(--tab-bottom) 100%);
    text-align: center; color: var(--white);
  }
  .title-kicker {
    font-family: "Questrial", sans-serif; font-size: 15px; letter-spacing: 6px;
    color: rgba(255,255,255,.75); margin-top: 6px;
  }
  .title-main {
    font-weight: 800; font-size: 62px; line-height: 1; letter-spacing: 1px; margin-top: 6px;
  }

  .photo {
    position: absolute; top: 0; background: var(--white); padding: 8px;
    box-shadow: 0 3px 10px rgba(0,0,0,.45);
  }
  .photo-fill { width: 100%; height: 100%; }
  .photo--house  { left: 18px;  top: 186px; width: 220px; height: 170px; transform: rotate(-2deg); }
  .photo--house .photo-fill  { background: linear-gradient(180deg, #c9d4dc 0%, #5e5a4d 50%, #6d8a4a 100%); }
  .photo--dining { left: 248px; top: 192px; width: 224px; height: 170px; transform: rotate(3deg); }
  .photo--dining .photo-fill { background: linear-gradient(135deg, #e0a05a 0%, #c77a2d 60%, #8a4e1c 100%); }
  .photo--heater { left: 478px; top: 182px; width: 226px; height: 174px; transform: rotate(-2deg); }
  .photo--heater .photo-fill { background: linear-gradient(180deg, #d8a66a 0%, #6b4a36 55%, #b9a089 100%); }
  .photo--sea    { left: 712px; top: 186px; width: 220px; height: 168px; transform: rotate(2deg); }
  .photo--sea .photo-fill    { background: linear-gradient(180deg, #b8d0e4 0%, #4a88b8 45%, #4f7a3c 100%); }

  .features {
    position: absolute; left: 0; top: 403px; width: 100%; height: 204px;
    background: var(--panel);
    display: flex; padding: 22px 0 0 64px;
  }
  .feature-list {
    list-style: none; width: 428px;
    font-weight: 600; font-size: 14.5px; line-height: 19.5px; color: var(--ink);
  }
  .feature-list li { position: relative; padding-left: 22px; }
  .feature-list li::before {
    content: ""; position: absolute; left: 0; top: 7px;
    width: 7px; height: 7px; border-radius: 50%; background: var(--ink);
  }
  .feature-list .indent { padding-left: 22px; }
  .feature-list .indent::before { display: none; }

  .contact-bar {
    position: absolute; left: 0; top: 607px; width: 100%; height: 50px;
    background: var(--cyan); color: var(--white);
    display: flex; align-items: center; padding-left: 22px; white-space: nowrap;
  }
  .contact-lead { font-family: "Questrial", sans-serif; font-size: 25px; }
  .contact-strong { font-weight: 800; font-size: 30px; margin-left: 10px; }
</style>
</head>
<body>
  <article class="leaflet">
    <div class="header-band"></div>

    <header class="title-tab">
      <p class="title-kicker">Book right now your</p>
      <h1 class="title-main">HOLIDAY SPECIAL</h1>
    </header>

    <figure class="photo photo--house"><div class="photo-fill" role="img" aria-label="Photo of the two-storey holiday house with timber deck and lawn"></div></figure>
    <figure class="photo photo--dining"><div class="photo-fill" role="img" aria-label="Photo of the timber-lined open plan dining area"></div></figure>
    <figure class="photo photo--heater"><div class="photo-fill" role="img" aria-label="Photo of the slow combustion wood heater in the lounge"></div></figure>
    <figure class="photo photo--sea"><div class="photo-fill" role="img" aria-label="Photo of the ocean view from the house"></div></figure>

    <section class="features">
      <ul class="feature-list">
        <li>Sleeps 8-10</li>
        <li class="indent">(2 Queen, 1 Double, 2 bunks), 4 bedrooms</li>
        <li>BIR to all bedrooms</li>
        <li>2 Bathrooms, one with bath, 2 toilets</li>
        <li>Open Plan Lounge/Dining/Kitchen area</li>
        <li>Dining Table for 8 people</li>
        <li>Reverse cycle air conditioner</li>
        <li>Slow combustion wood heater</li>
      </ul>
      <ul class="feature-list">
        <li>TV/DVD, CD/Radio</li>
        <li>Kitchen has m/wave, oven, fridge/freezer, dishwasher</li>
        <li>BBQ provided</li>
        <li>Timber decking with 2 outside tables and 12 chairs</li>
        <li>Washing Machine and dryer provided</li>
        <li>One street back from beach</li>
        <li>Smoke free zone</li>
        <li>No Pets</li>
      </ul>
    </section>

    <footer class="contact-bar">
      <span class="contact-lead">For further information or to book contact</span>
      <span class="contact-strong">Joan on 0491 287 306</span>
    </footer>
  </article>
</body>
</html>
```